Brochure Design Project

Check our www.harbourlanehomes.example. Company Name is "Harbour Lane Living" and the brochure is to be named "Golden Tides Ahead".

We are seeking a brochure that captures the essence of the idea of living aboard a cruise ship in retirement therefore must encompass not only cruising but also retirement living, therefore we're promoting "a lifestyle better than living ashore in a retirement village".

Brochure will be around 20+ pages though there will only most likely only be around 6 pages of actual templates needed which can be used interchangeably plus a front and back cover.

Some pictures on the brochure will take up full pages with maybe a caption so these other pages should be pretty quick.

Must have great presence and "feel" about it.

Friendly, cheery brochure with bright colours.

Must "look a million dollars" as the market we're targeting is very selective and we're competing in a very competitive market, retirement villages where our clientele is investing large sums of money in their retirement and they are basing their decision on whether to trust us on possibly only this brochure.

This is a new project that will launch on television, radio, pamphlet and brochure in the next 6 weeks.

Work on a brochure I'd been doing attached. Don't just want a repeat of this brochure. This is to provide you with various pieces of text to start the brochure, not to copy the design, which I think is antique and needs completely redoing.

Project Deadline Extended
Reason: At present we have only received a few designs and at present none of them are truly suitable to what we're after or require quite a few changes in terms of creativity to even come close to what we'd be expecting from professional graphic designers.

Project Deadline Extended
Reason: New designers have accepted the invitation to submit designs and many have only had a couple of days to submit designs.

If you haven't already submitted your final designs, please finalise and submit them. Deadline is almost reached.

We look forward to the seeing the final submissions.

Regards,

Harbour Lane Living Ltd.

50+ age bracket (therefore larger writing for brochure text)

Radio

Must have
• We are after classy and sophisticated, not gaudy and cheap so the design must look formal yet modern and eschew the virtues of contemporary and exotic and a higher standard of retirement living rather than "bright, gaudy, cheap and a quick buck".

Our company is designed to provide sophisticated and practical living arrangements for people that are looking for comfortable, practical yet stylishly different in terms of the elegance and lifestyle that people would normally expect for the price of standard living arrangements.

Brochure when completed must be sent in an editable format rather than just static.

Must have a section for pricing comparison between costs of living in "Own Home vs. Retirement Village vs. Harbour Lane Living" for comparision of costs.

Must also have a second comparison with the same titles though this is a "Features/Facilities Comparison".

Must use only royalty-free photography.

Must NOT use pictures of GIANT cruise ships. The ships we're providing our clientelle are mid-1990's ships therefore have a capacity of around 800-1000 capacity, not like today's MEGA-liners that hold 2000-5000 passengers. We don't want to mislead our clientele.

Must NOT use pictures of ships with any names or logos on them (to forestall the possibility of copyright and trademark infringement).

```html
<!DOCTYPE html>
<html lang="en">
<head>
<meta charset="utf-8">
<title>Golden Tides Ahead – Harbour Lane Living brochure</title>
<link rel="stylesheet" href="https://fonts.googleapis.com/css2?family=Great+Vibes&family=Lora:ital,wght@0,600;1,400&family=Open+Sans:wght@400;600;700&display=swap">
<style>
  :root {
    --backdrop: #e9e7e3;
    --paper: #ffffff;
    --navy: #1d2657;
    --navy-deep: #141b45;
    --blue: #1f6fb6;
    --blue-light: #4a9ad8;
    --gold: #d8a11c;
    --ink: #33373f;
    --ink-soft: #6a6f7a;
  }
  * { box-sizing: border-box; margin: 0; padding: 0; }
  html, body { width: 1200px; height: 720px; overflow: hidden; }
  body {
    background: var(--backdrop);
    font-family: "Open Sans", Arial, sans-serif;
    color: var(--ink);
    position: relative;
  }

  /* ---------- open spread ---------- */
  .spread {
    position: absolute; left: 40px; top: 105px;
    width: 720px; height: 509px;
    display: flex;
    box-shadow: 0 6px 18px rgba(0,0,0,.15);
  }
  .page {
    width: 360px; height: 509px;
    background: var(--paper);
    position: relative;
    overflow: hidden;
  }
  .page--left { border-right: 1px solid #d6d6d6; }

  .section-tab {
    position: absolute; left: 0; top: 22px;
    width: 100%; height: 26px;
    background: linear-gradient(90deg, var(--blue) 0%, var(--blue-light) 100%);
    color: #fff; font-size: 12px; font-weight: 600;
    padding: 5px 22px; letter-spacing: .3px;
  }
  .photo { position: absolute; }
  .photo--couple-dining {
    left: 0; top: 48px; width: 100%; height: 232px;
    background: linear-gradient(135deg, #4f6a3a 0%, #9a7b5a 45%, #e2c3a3 70%, #2a2a2a 100%);
  }
  .body-copy {
    font-size: 11px; line-height: 1.6; color: var(--ink);
  }
  .page--left .body-copy {
    position: absolute; left: 22px; right: 22px; top: 294px;
  }
  .page-number {
    position: absolute; bottom: 12px; font-size: 10px; color: var(--ink-soft);
  }
  .page--left .page-number { left: 22px; }
  .page--right .page-number { right: 22px; }

  .page--right .intro {
    position: absolute; left: 22px; right: 22px; top: 24px;
  }
  .feature-band {
    position: absolute; left: 0; top: 186px; width: 100%; height: 140px;
    background: var(--blue);
  }
  .feature-band__caption {
    position: absolute; left: 0; top: 0; width: 100%; height: 24px;
    background: var(--navy);
    color: #fff; font-size: 12px; font-weight: 600;
    padding: 4px 22px;
  }
  .photo--lounge-deck {
    left: 14px; top: 32px; width: 332px; height: 100px;
    background: linear-gradient(180deg, #bfe0f4 0%, #6aaed8 45%, #2f6e9e 100%);
  }
  .page--right .closing {
    position: absolute; left: 22px; right: 22px; top: 338px;
  }

  /* ---------- front cover ---------- */
  .cover {
    position: absolute; left: 810px; top: 105px;
    width: 360px; height: 509px;
    background: var(--paper);
    overflow: hidden;
    box-shadow: 0 6px 18px rgba(0,0,0,.15);
  }
  .cover__masthead {
    height: 100px;
    background: linear-gradient(180deg, var(--navy-deep), var(--navy));
    color: #fff;
    display: flex; align-items: baseline; justify-content: center;
    padding-top: 26px; gap: 8px;
    font-family: "Great Vibes", cursive;
  }
  .cover__title-lead { font-size: 20px; color: #e8e3d2; }
  .cover__title-main { font-size: 52px; color: #fff; line-height: 1; }
  .photo--couple-on-deck {
    left: 0; top: 100px; width: 100%; height: 250px;
    background: linear-gradient(180deg, #cfe6f6 0%, #a9cfe9 40%, #e8eef2 70%, #8b6a4a 100%);
  }
  .cover__brand-band {
    position: absolute; left: 0; top: 300px; width: 100%; height: 120px;
    background: var(--paper);
    clip-path: polygon(0 42%, 100% 0, 100% 100%, 0 100%);
  }
  .brand {
    position: absolute; right: 30px; top: 350px;
    display: flex; align-items: center; gap: 8px;
    font-family: "Lora", Georgia, serif; font-weight: 600;
    font-size: 20px; color: var(--gold);
  }
  .brand__dot {
    width: 10px; height: 10px; border-radius: 50%; background: var(--gold);
  }
  .cover__web {
    position: absolute; right: 30px; top: 382px;
    font-size: 9px; color: var(--navy);
  }
  .cover__tagline-band {
    position: absolute; left: 0; bottom: 0; width: 100%; height: 80px;
    background: var(--navy);
    border-top: 3px solid var(--gold);
    display: flex; align-items: center; justify-content: center;
    padding: 0 20px;
  }
  .cover__tagline {
    font-family: "Lora", Georgia, serif; font-style: italic;
    font-size: 13px; line-height: 1.45; color: #f2e6c4; text-align: center;
  }
</style>
</head>
<body>

<section class="spread" aria-label="Inside spread">
  <article class="page page--left">
    <h2 class="section-tab">We are a floating village</h2>
    <div class="photo photo--couple-dining" role="img" aria-label="Photo of a smiling retired couple sharing a glass of wine at dinner"></div>
    <p class="body-copy">A home at sea offers the calm of a private residence with the variety of a new port every few days. Residents keep their own cabin, dine in elegant rooms and enjoy friendly staff who know them by name. Every meal, every trip ashore and every evening show is part of one simple monthly fee, so there are no surprise bills. Days can be as busy or as quiet as you wish, from classes and dancing to long afternoons reading on deck in the sun.</p>
    <span class="page-number">4</span>
  </article>

  <article class="page page--right">
    <p class="body-copy intro">Our ships are mid-sized vessels built for comfort rather than crowds. With fewer than a thousand guests on board, neighbours soon become friends and the decks never feel busy. Medical care is close at hand, housekeeping is daily and there is always a quiet corner to read, paint or simply watch the horizon drift by. Each port brings new markets, walks and friendly faces to enjoy.</p>
    <div class="feature-band">
      <h3 class="feature-band__caption">Sea views we can give you every day</h3>
      <div class="photo photo--lounge-deck" role="img" aria-label="Photo of a bright ship lounge with blue seating and ocean view"></div>
    </div>
    <p class="body-copy closing">Compared with a retirement village, life aboard costs about the same yet includes travel, fine dining and entertainment. You can stay for a season or for many years, and family are always welcome to visit at any port along the way. Our team handles every detail, from moving in to planning your first voyage.</p>
    <span class="page-number">5</span>
  </article>
</section>

<section class="cover" aria-label="Front cover">
  <header class="cover__masthead">
    <span class="cover__title-lead">Golden Tides</span>
    <span class="cover__title-main">Ahead</span>
  </header>
  <div class="photo photo--couple-on-deck" role="img" aria-label="Photo of a retired couple chatting at the railing of a ship deck"></div>
  <div class="cover__brand-band"></div>
  <div class="brand"><span class="brand__dot"></span>Harbour Lane Living</div>
  <span class="cover__web">www.harbourlanehomes.example</span>
  <footer class="cover__tagline-band">
    <p class="cover__tagline">A lifestyle better than living ashore in a retirement village</p>
  </footer>
</section>

</body>
</html>
```